Nareem Advertising & Publicity business cards

I would like my Company's business card to be designed creatively & profissionally the logo is attached in both Arabic & english and prefer to have my emblem dimmed on the card as well
-Logo ( Arabic & English)
-Name (Arabic & English)
-Title ( Arabic & English)
-----------
-Location
-Landline (icon)
-Mobile phone (icon)
-Email (icon)
-Instagram (icon)
-WhatsApp (icon)

Target Market(s)

Industry/Entity Type

Marketing

Contact Information for Business Card

-Logo ( Arabic & English)
-Name (Arabic & English)
-----------
-Location
-Landline (icon)
-Mobile phone (icon)
-Email (icon)
-Instagram (icon)
-WhatsApp (icon)

Font styles to use
Serif

Requirements
Must have
• all what is mentions in business card details blanked and i will add the data my self
Nice to have
• Dim emblem on my business card both Arabic & english

```html
<!DOCTYPE html>
<html lang="en">
<head>
<meta charset="utf-8">
<title>Nareem Advertising &amp; Publicity – Business Card</title>
<link rel="stylesheet" href="https://fonts.googleapis.com/css2?family=Sorts+Mill+Goudy&family=Arimo:wght@400;700&display=swap">
<style>
  :root{
    --sheet-light:#f4f4f4;
    --sheet-light-edge:#e6e6e6;
    --sheet-dark:#0e0e0e;
    --navy:#06066e;
    --card-white:#fbfbfb;
    --ink:#1f1f1f;
    --mark-grey:#333436;
    --teal:#5cc6bd;
    --rule-blue:#4aa7d6;
    --icon-blue:#3c8fd0;
    --white:#ffffff;
  }
  *{box-sizing:border-box;margin:0;padding:0}
  html,body{width:1200px;height:999px;overflow:hidden}
  body{position:relative;font-family:"Arimo",Arial,sans-serif;background:var(--sheet-dark)}

  .sheet-light{position:absolute;left:0;top:0;width:1200px;height:497px;
    background:radial-gradient(ellipse at 55% 40%,var(--sheet-light) 0%,var(--sheet-light) 45%,var(--sheet-light-edge) 100%)}
  .sheet-dark{position:absolute;left:0;top:497px;width:1200px;height:502px;background:var(--sheet-dark)}

  .card{position:absolute;overflow:hidden;box-shadow:0 12px 22px rgba(0,0,0,.28)}
  .card-front{left:40px;top:93px;width:649px;height:355px;background:var(--card-white)}
  .card-back{left:482px;top:573px;width:648px;height:355px;
    background:radial-gradient(ellipse at 50% 45%,#1e1eb4 0%,#0c0c94 45%,var(--navy) 100%)}

  .band{position:absolute;left:0;width:100%;height:41px}
  .band svg{display:block;width:100%;height:100%}
  .band-top{top:0}
  .band-bottom{bottom:0}

  .faint-emblem{position:absolute;left:585px;top:120px;width:130px;height:210px;
    background:radial-gradient(ellipse at center,rgba(120,120,200,.12),rgba(120,120,200,0) 70%)}

  .name{position:absolute;font-family:"Sorts Mill Goudy",Georgia,serif;font-weight:400;font-size:24px;color:var(--ink);
    white-space:nowrap;padding-bottom:1px;border-bottom:1px solid #8f8fd0}
  .name-en{left:18px;top:52px;width:214px}
  .name-ar{left:421px;top:53px;width:208px}
  .title{position:absolute;font-family:"Sorts Mill Goudy",Georgia,serif;font-weight:700;font-size:14px;color:var(--ink)}
  .title-en{left:195px;top:89px}
  .title-ar{left:600px;top:89px}

  .divider{position:absolute;left:330px;top:97px;width:2px;height:165px;background:var(--rule-blue)}

  .contact-list{position:absolute;left:348px;top:116px;list-style:none}
  .contact-list li{display:flex;align-items:center;height:24.8px;font-size:16px;color:#222;white-space:nowrap}
  .contact-list svg{width:14px;height:14px;margin-right:63px;flex:none}
  .contact-list b{font-weight:700;margin:0 5px}

  .location{position:absolute;left:155px;top:274px;font-family:"Sorts Mill Goudy",Georgia,serif;font-size:16px;color:var(--ink);white-space:nowrap}
  .location .sep{display:inline-block;width:1px;height:22px;background:#9a9ad6;vertical-align:middle;margin:0 6px}

  .wordmark{position:absolute;display:flex;align-items:center;gap:14px}
  .wordmark .swatch{flex:none}
  .wordmark .label{font-family:"Arimo",Arial,sans-serif;font-weight:700;line-height:1.15;white-space:nowrap}

  .wm-front{left:78px;top:150px}
  .wm-front .swatch{width:44px;height:44px;background:var(--teal)}
  .wm-front .label{font-size:16px;color:var(--mark-grey)}

  .wm-display{left:790px;top:220px}
  .wm-display .swatch{width:74px;height:74px;background:var(--teal)}
  .wm-display .label{font-size:22px;color:var(--mark-grey)}

  .wm-dark{left:56px;top:714px}
  .wm-dark .swatch{width:78px;height:78px;background:var(--white)}
  .wm-dark .label{font-size:25px;color:var(--white)}

  .wm-back{left:150px;top:141px}
  .wm-back .swatch{width:78px;height:78px;background:var(--white)}
  .wm-back .label{font-size:25px;color:var(--white)}
</style>
</head>
<body>
  <div class="sheet-light"></div>
  <div class="sheet-dark"></div>

  <section class="card card-front">
    <div class="band band-top">
      <svg viewBox="0 0 649 41" preserveAspectRatio="none">
        <defs>
          <linearGradient id="bandA" x1="0" x2="1"><stop offset="0" stop-color="#b4b4e2"/><stop offset=".45" stop-color="#0b0b7c"/><stop offset=".7" stop-color="#09097a"/><stop offset="1" stop-color="#4444cf"/></linearGradient>
        </defs>
        <rect width="649" height="41" fill="url(#bandA)"/>
        <polygon points="0,0 330,0 0,41" fill="#c8c8ec" opacity=".45"/>
        <polygon points="649,0 649,41 300,41" fill="#3a3acc" opacity=".45"/>
      </svg>
    </div>
    <div class="faint-emblem" role="img" aria-label="Faint company emblem decoration"></div>

    <h2 class="name name-en">Your Name (English)</h2>
    <p class="title title-en">Title</p>
    <h2 class="name name-ar">Your Name (Arabic)</h2>
    <p class="title title-ar">Title</p>

    <div class="wordmark wm-front">
      <span class="swatch"></span>
      <span class="label">Nareem Advertising<br>&amp; Publicity</span>
    </div>

    <div class="divider"></div>

    <ul class="contact-list">
      <li><svg viewBox="0 0 16 16"><path d="M4 1l3 3-2 2c1 2 3 4 5 5l2-2 3 3-2 3C7 15 1 9 1 3z" fill="var(--icon-blue)"/></svg>English<b>|</b>Arabic</li>
      <li><svg viewBox="0 0 16 16"><rect x="4" y="1" width="8" height="14" rx="1.5" fill="none" stroke="#7a6fd6" stroke-width="1.6"/><circle cx="8" cy="12.5" r=".9" fill="#7a6fd6"/></svg>English<b>|</b>Arabic</li>
      <li><svg viewBox="0 0 16 16"><rect x="1" y="3" width="14" height="10" fill="var(--icon-blue)"/><path d="M1 3l7 6 7-6" fill="none" stroke="#fff" stroke-width="1.2"/></svg>English<b>|</b>Arabic</li>
      <li><svg viewBox="0 0 16 16"><circle cx="8" cy="8" r="7" fill="var(--icon-blue)"/></svg>English<b>|</b>Arabic</li>
      <li><svg viewBox="0 0 16 16"><circle cx="8" cy="8" r="7" fill="#4c9fcf"/></svg>English<b>|</b>Arabic</li>
    </ul>

    <p class="location">Your Location (English)<span class="sep"></span>Your Location (Arabic)</p>

    <div class="band band-bottom">
      <svg viewBox="0 0 649 41" preserveAspectRatio="none">
        <defs>
          <linearGradient id="bandB" x1="0" x2="1"><stop offset="0" stop-color="#a0a0da"/><stop offset=".4" stop-color="#0b0b7c"/><stop offset=".7" stop-color="#0a0a7a"/><stop offset="1" stop-color="#4848d2"/></linearGradient>
        </defs>
        <rect width="649" height="41" fill="url(#bandB)"/>
        <polygon points="0,0 0,41 340,41" fill="#c0c0ea" opacity=".4"/>
        <polygon points="649,0 300,0 649,41" fill="#3a3acc" opacity=".45"/>
      </svg>
    </div>
  </section>

  <div class="wordmark wm-display">
    <span class="swatch"></span>
    <span class="label">Nareem Advertising<br>&amp; Publicity</span>
  </div>

  <div class="wordmark wm-dark">
    <span class="swatch"></span>
    <span class="label">Nareem Advertising<br>&amp; Publicity</span>
  </div>

  <section class="card card-back">
    <div class="band band-top">
      <svg viewBox="0 0 648 41" preserveAspectRatio="none">
        <rect width="648" height="41" fill="url(#bandA)"/>
        <polygon points="0,0 330,0 0,41" fill="#c8c8ec" opacity=".45"/>
        <polygon points="648,0 648,41 300,41" fill="#3a3acc" opacity=".45"/>
      </svg>
    </div>
    <div class="wordmark wm-back">
      <span class="swatch"></span>
      <span class="label">Nareem Advertising<br>&amp; Publicity</span>
    </div>
    <div class="band band-bottom">
      <svg viewBox="0 0 648 41" preserveAspectRatio="none">
        <rect width="648" height="41" fill="url(#bandB)"/>
        <polygon points="0,0 0,41 340,41" fill="#c0c0ea" opacity=".4"/>
        <polygon points="648,0 300,0 648,41" fill="#3a3acc" opacity=".45"/>
      </svg>
    </div>
  </section>
</body>
</html>
```